bargainmentor.net - Podcast Guest Marketing E-Flyer PDF

Dear Designers:I am in need of an attractive and attention-getting layout and design for a three-page marketing flyer (commonly known as a media one sheet) that will be sent via e-mail, as PDF file, to various Podcast hosts to market me as a guest on their podcasts. I want the design of the document to "mirror" the design and branding on my parent bargainmentor.net website. I am providing ALL the edited and proofread copy and content - the designer just needs to create the design for this marketing document. I want an active PDF document and icons should be used for LinkedIn, Phone, E-mail , and website- with hyperlinks that connect accordingly. I need a fast turnaround.
Updates

Dear Designers - instead of using the photo in the project file of me speaking to the audience for the banner image - I thought it would be a better idea to make this marketing piece specific to Podcast Hosts. Therefore, an image such as the one in the link below would be good to use for a banner image. https://www.pixtrove-example.net/gallery?topic=recording+booth+images&ref=qz7&view=grid&id=Kx93LmPwa2RtVbN8YcQdE4&w=1377&h=804#pic=vRmalqobet:

Target Market(s)

This PDF document will be sent to 650 Podcast hosts in North America via a broadcast e-mail.

Font styles to use
Sans Serif

Colors
ec1f27
ffffff
000000
333333
9d9d9d

Requirements
Must have
• A three-page layout that is easy to navigate in PDF form.
• Proper font styles and sizes for key emphasis areas on the document/
• Consistent branding to mirror my bargainmentor.net parent website
• Must be easy for people to read
• Attention-getting design elements and layout
• Professional and sophisticated design
• Icons for contact information
Should not have
• Should not be cluttered and junky-looking.
• Should not use small font sizes that makes it difficult to read.
• If Podcast hosts are interested in having me as a guest - they will read the content as required on three-pages

```html
<!DOCTYPE html>
<html lang="en">
<head>
<meta charset="utf-8">
<title>bargainmentor.net – Podcast Guest One Sheet</title>
<link href="https://fonts.googleapis.com/css2?family=Roboto:ital,wght@0,400;0,500;0,700;1,400&family=Open+Sans:ital,wght@0,400;0,600;1,400&display=swap" rel="stylesheet">
<style>
:root{
  --red:#ec1f27;
  --white:#ffffff;
  --black:#000000;
  --ink:#333333;
  --grey:#9d9d9d;
  --backdrop:#929292;
  --dark:#2e2e30;
}
*{margin:0;padding:0;box-sizing:border-box}
html,body{width:1200px;height:1200px;overflow:hidden}
body{background:var(--backdrop);font-family:'Open Sans',sans-serif;color:var(--ink);position:relative}
.page{position:absolute;width:395px;height:554px;background:var(--white);box-shadow:3px 6px 10px rgba(0,0,0,.35);overflow:hidden}
.page-1{left:116px;top:42px}
.page-2{left:684px;top:42px}
.page-3{left:388px;top:629px}
.abs{position:absolute}
.brand{left:0;right:0;top:18px;display:flex;justify-content:center;align-items:center;gap:6px}
.brand-mark{width:20px;height:20px;background:var(--red)}
.brand-name{font-family:'Roboto',sans-serif;font-size:20px;font-weight:400;color:var(--ink);letter-spacing:-.3px}
.hero-photo{left:0;top:50px;width:395px;height:150px;background:linear-gradient(180deg,#3a3a3c,#1f1f21)}
.hero-band{left:0;top:198px;width:395px;height:51px;background:var(--dark);color:var(--white);font-family:'Roboto',sans-serif;font-weight:500;font-size:9.4px;line-height:11.6px;text-align:center;padding:6px 16px 0}
.portrait{left:14px;top:114px;width:80px;height:80px;border-radius:50%;border:3px solid var(--white);background:linear-gradient(160deg,#8a8a8a,#3d3d3d)}
.intro-box{left:95px;top:145px;width:233px;height:41px;background:var(--red);color:var(--white);font-family:'Roboto',sans-serif;font-size:8.6px;line-height:11px;padding:9px 0 0 13px}
.intro-box strong{font-size:11px;font-weight:500}
.sec-head{left:0;display:flex;align-items:center;gap:4px;font-family:'Roboto',sans-serif;font-size:9.6px;color:var(--ink)}
.sec-head::before{content:"";display:block;width:22px;height:9px;background:var(--red)}
.body-copy{font-size:5.4px;line-height:7.4px;color:var(--ink);text-align:justify}
.reasons{left:22px;top:356px;width:362px;display:grid;grid-template-columns:1fr 1fr;column-gap:16px}
.reason{display:flex;gap:3px;margin-bottom:11px}
.num{flex:0 0 9px;height:8px;background:var(--ink);color:var(--white);font-size:5.5px;font-weight:600;text-align:center;line-height:8px}
.footer{left:0;bottom:0;width:395px;height:27px;background:var(--dark);display:flex;align-items:center;font-family:'Roboto',sans-serif;color:var(--white)}
.footer-phone{position:relative;height:27px;width:112px;background:var(--red);display:flex;align-items:center;padding-left:12px;gap:3px;font-size:10px;font-weight:700;clip-path:polygon(0 0,92% 0,100% 100%,0 100%)}
.footer-links{display:flex;gap:12px;font-size:6.2px;margin-left:2px}
.footer-links span{display:flex;align-items:center;gap:2px}
.top-bar{left:0;top:0;width:310px;height:18px;background:#1c1c1c}
.outlets{left:24px;top:174px;width:353px;height:73px;border:1px solid var(--grey);display:grid;grid-template-columns:repeat(3,1fr);align-content:center;row-gap:14px;padding:0 8px;font-family:'Roboto',sans-serif}
.outlet{font-size:11px;font-weight:700;color:var(--ink);text-align:center;white-space:nowrap}
.outlet.wide{grid-column:span 2;font-size:13px}
.ways{left:38px;width:335px}
.way{display:flex;gap:4px}
.red-banner{left:13px;top:432px;width:368px;height:91px;background:linear-gradient(135deg,#e4262c,#b3161b)}
.event-photo{left:0;top:0;width:395px;height:159px;background:linear-gradient(180deg,#7b3a3a 0%,#5d5450 45%,#2f2d2e 100%)}
.quote{display:flex;gap:3px;font-size:6.4px;line-height:8.8px;font-style:italic;color:var(--ink)}
.qmark{color:var(--red);font-family:'Roboto',sans-serif;font-weight:700;font-size:13px;line-height:10px}
.sig{font-family:'Roboto',sans-serif;font-size:6.2px;line-height:8.2px;font-weight:500;color:var(--black)}
</style>
</head>
<body>

<!-- Page 1 -->
<section class="page page-1">
  <div class="abs brand"><span class="brand-mark"></span><span class="brand-name">bargainmentor</span></div>
  <div class="abs hero-photo" role="img" aria-label="Speaker presenting to a seated audience at a seminar, darkened monochrome"></div>
  <div class="abs portrait" role="img" aria-label="Head-and-shoulders portrait of the speaker"></div>
  <div class="abs intro-box">Meet Bargain Mentor® <strong>Daniel R. Marston</strong><br>–The Expert You Need As a Guest on Your Podcast</div>
  <div class="abs hero-band">Are you looking for a relevant and appealing topic and an engaging subject matter expert who can provide measurable value and life-changing tips to the listeners of your podcast?</div>

  <h2 class="abs sec-head" style="top:262px">Why Negotiating and Decision Making Should Be Topics on Your Podcast?</h2>
  <p class="abs body-copy" style="left:25px;top:278px;width:355px">Regardless of your podcast theme – it's important to remember that your listeners are negotiating all the time – in their personal lives, social lives, and especially in their business lives. Negotiating is an essential life skill. Everyone can improve his or her negotiating skills, and Daniel is the expert who can provide the answers your people crave. Your podcast listeners will benefit from Daniel's proven, practical, and relevant negotiating strategies and tips that will improve results and outcomes in all types of personal and business negotiations.</p>

  <h2 class="abs sec-head" style="top:339px">Six Reasons to Book Daniel R. Marston As a Guest on Your Podcast</h2>
  <div class="abs reasons">
    <div>
      <div class="reason"><span class="num">1</span><p class="body-copy">Daniel is a dynamic, thought-provoking, engaging, captivating, and entertaining speaker who will share some great personal stories to help your listeners better understand and relate to the topic of negotiating and decision-making dynamics. He will indeed challenge the "status quo."</p></div>
      <div class="reason"><span class="num">2</span><p class="body-copy">Daniel is the founder of bargainmentor.net and is an internationally recognized expert and highly rated speaker on the topics of negotiating and decision-making dynamics that affect negotiated outcomes. His versatility and commitment to proper preparation will ensure that his content is tailored to address the theme of your podcast and the needs of your listeners.</p></div>
      <div class="reason"><span class="num">3</span><p class="body-copy">His five-star-rated presentations and training programs have been delivered around the world to small and medium-sized businesses, Top 500 corporations, and large industry, trade, and peer-to-peer associations such as Emerging Leaders' Council and Founders' Circle.</p></div>
    </div>
    <div>
      <div class="reason"><span class="num">4</span><p class="body-copy">Daniel has personally trained over 50,000 people of all experience levels, across multiple industries, in 31 countries how to negotiate more effectively.</p></div>
      <div class="reason"><span class="num">5</span><p class="body-copy">With formal training in broadcasting and media arts, Daniel provides 30 years of experience as a professional speaker who can provide your listeners with valuable insights, solutions, and answers to address listeners' challenges and questions.</p></div>
      <div class="reason"><span class="num">6</span><p class="body-copy">Daniel is the creator of the best-selling Deal Strength Toolkit Audio Learning Program – designed to be an effective all-in-one learning solution that helps people improve their negotiating capabilities and skills. He is also the host of his soon-to-be-launched Podcast – Deal Talk Daily.</p></div>
    </div>
  </div>

  <footer class="abs footer">
    <div class="footer-phone"><svg width="8" height="8" viewBox="0 0 24 24"><path fill="#fff" d="M6.6 10.8a15 15 0 0 0 6.6 6.6l2.2-2.2c.3-.3.7-.4 1-.2 1.1.4 2.3.6 3.6.6.6 0 1 .4 1 1V20c0 .6-.4 1-1 1A17 17 0 0 1 3 4c0-.6.4-1 1-1h3.5c.6 0 1 .4 1 1 0 1.3.2 2.5.6 3.6.1.3 0 .7-.2 1z"/></svg>555-014-2739</div>
    <div class="footer-links">
      <span><svg width="5" height="5"><circle cx="2.5" cy="2.5" r="2.2" fill="none" stroke="#fff" stroke-width=".8"/></svg>bargainmentor.net</span>
      <span><svg width="6" height="4"><rect x=".4" y=".4" width="5.2" height="3.2" fill="none" stroke="#fff" stroke-width=".8"/></svg>daniel@marstonmail.net</span>
      <span><svg width="5" height="5"><rect x=".4" y=".4" width="4.2" height="4.2" fill="none" stroke="#fff" stroke-width=".8"/></svg>network.example/in/danielmarston</span>
    </div>
  </footer>
</section>

<!-- Page 2 -->
<section class="page page-2">
  <div class="abs top-bar"></div>
  <h2 class="abs sec-head" style="top:44px">How Podcast Listeners Will Benefit</h2>
  <div class="abs body-copy" style="left:26px;top:59px;width:355px">
    <p>Most people are intimidated by the prospect and process of negotiating – and often view negotiating as an uncomfortable haggling and bargaining process that may involve confrontation, anxiety, and stress.<br>If podcast listeners are like most people – then they probably are concerned about being taken advantage of – or that they are missing out on potential opportunities in their personal, social, and business negotiations.</p>
    <p style="margin-top:7px">To alleviate your listeners' concerns, Daniel will provide them with easy-to-understand negotiating strategies, tactics, phrases, and tips they can immediately apply – the moment the podcast episode ends. Your listeners will feel more confident when they are equipped with the powerful and beneficial strategies and techniques that will help them save/make money and arrive at better outcomes when negotiating with customers, clients, suppliers, contractors, financial institutions, retailers, co-workers, colleagues, and family members.<br>Daniel R. Marston in the Media</p>
  </div>
  <p class="abs body-copy" style="left:24px;top:157px;font-size:6px;font-weight:600">Daniel has appeared on radio programs, written articles or contributed to articles for the following media outlets:</p>
  <div class="abs outlets">
    <span class="outlet">The Harbour Ledger</span>
    <span class="outlet">Capitalist Weekly</span>
    <span class="outlet">Sales Summit</span>
    <span class="outlet">Venture Forum</span>
    <span class="outlet wide">Market Journal Daily</span>
  </div>

  <h2 class="abs sec-head" style="top:270px">Three Ways You Can Profit From Booking Daniel R. Marston on Your Podcast</h2>
  <p class="abs body-copy" style="left:29px;top:285px;width:345px;font-size:6.8px;line-height:9px">Upon mutual agreement, podcast hosts and listeners can have access to the following money-saving and profit-generating opportunities:</p>
  <div class="abs ways" style="top:316px"><div class="way"><span class="num">1</span><p class="body-copy">Podcast hosts will be provided with a specific promotional code to share with your listeners that will entitle them to receive a special one-time discount of $19.95US off the purchase of the MP3 download of the Deal Strength Toolkit Audio Learning Program available on my online store. Complete download and purchase instructions will be provided to podcast hosts to publish in your notes and also communicate to your listeners.</p></div></div>
  <div class="abs ways" style="top:358px"><div class="way"><span class="num">2</span><p class="body-copy">Podcast hosts will receive a 10% commission payable on the net sales dollar revenue generated from the sale of MP3 downloads of Daniel's Deal Strength Toolkit Audio Learning Program.</p></div></div>
  <div class="abs ways" style="top:388px"><div class="way"><span class="num">3</span><p class="body-copy">Podcast hosts will receive a 10% referral fee for any corporation or association that books Daniel for a presentation, seminar, or learning workshop that directly results from my participation on your podcast.</p></div></div>
  <p class="abs body-copy" style="left:19px;top:416px;font-style:italic;font-size:5.8px">Note: Discount and commission payments are subject to agreement to standard terms and conditions.</p>
  <div class="abs red-banner" role="img" aria-label="Seminar audience photo with a red tint overlay"></div>

  <footer class="abs footer">
    <div class="footer-phone"><svg width="8" height="8" viewBox="0 0 24 24"><path fill="#fff" d="M6.6 10.8a15 15 0 0 0 6.6 6.6l2.2-2.2c.3-.3.7-.4 1-.2 1.1.4 2.3.6 3.6.6.6 0 1 .4 1 1V20c0 .6-.4 1-1 1A17 17 0 0 1 3 4c0-.6.4-1 1-1h3.5c.6 0 1 .4 1 1 0 1.3.2 2.5.6 3.6.1.3 0 .7-.2 1z"/></svg>555-014-2739</div>
    <div class="footer-links">
      <span><svg width="5" height="5"><circle cx="2.5" cy="2.5" r="2.2" fill="none" stroke="#fff" stroke-width=".8"/></svg>bargainmentor.net</span>
      <span><svg width="6" height="4"><rect x=".4" y=".4" width="5.2" height="3.2" fill="none" stroke="#fff" stroke-width=".8"/></svg>daniel@marstonmail.net</span>
      <span><svg width="5" height="5"><rect x=".4" y=".4" width="4.2" height="4.2" fill="none" stroke="#fff" stroke-width=".8"/></svg>network.example/in/danielmarston</span>
    </div>
  </footer>
</section>

<!-- Page 3 -->
<section class="page page-3">
  <div class="abs event-photo" role="img" aria-label="Speaker presenting at a banquet-hall event to a large seated audience, red curtains behind"></div>
  <h2 class="abs sec-head" style="top:171px">Testimonials: What Some Clients Are Saying About the Bargain Mentor®</h2>
  <div class="abs" style="left:26px;top:192px;width:340px">
    <div class="quote"><span class="qmark" style="color:var(--ink);font-size:18px">“</span><p>Daniel Marston did a terrific job on my podcast. His negotiating insights and tips were well received by my listeners, and he was an engaging, knowledgeable, and entertaining guest. Given my expertise in real estate, I thought I was a good negotiator – until Daniel taught me a few new strategies and tips during the podcast. I would recommend Daniel to any podcast host – he is a pro and his topics are relevant and can benefit everyone.</p></div>
  </div>
  <div class="abs qmark" style="left:346px;top:242px;color:var(--ink);font-size:18px">”</div>
  <p class="abs sig" style="left:202px;top:250px;font-weight:400">- Curtis Allard<br>&nbsp; Podcast Host<br>&nbsp; Property Builders Podcast, San Antonio, Texas</p>

  <h2 class="abs sec-head" style="top:291px;align-items:flex-start;line-height:11px">Below is a partial listing of testimonials from attendees at an Founders' Circle (FC)<br>event provided by the RT Hollings, Chapter Learning Chair.</h2>
  <div class="abs" style="left:24px;top:327px;width:342px">
    <div class="quote"><span class="qmark">“</span><p>A very engaging, entertaining, and inspirational speaker who provided very useful information, strategies, and tips to apply to all my future negotiations.</p></div>
    <div class="quote" style="margin-top:16px"><span class="qmark">“</span><p>Thank you to FC Western New York for booking this speaker! I learned some things that I can address immediately and a lot material that I need to practice. Great session!</p></div>
    <div class="quote" style="margin-top:16px"><span class="qmark">“</span><p>Daniel was an outstanding speaker on the topic of negotiating! He was one of my favorite speakers ever! Daniel was a real 'teacher' versus other typical speakers who spend two hours bragging or promoting their book.</p></div>
    <div class="quote" style="margin-top:16px"><span class="qmark">“</span><p>Daniel was a very knowledgeable and well-prepared speaker who provided helpful tips and scripts throughout the entire presentation! I would love to learn more from this speaker.</p></div>
  </div>
  <p class="abs sig" style="left:36px;top:474px">RT Hollings, CEO and President<br>Northgate Records Group<br>Founders' Circle (FC) Western New York<br>Learning Chair</p>
  <h3 class="abs" style="left:22px;top:513px;font-family:'Roboto',sans-serif;font-weight:500;font-size:9.4px;color:var(--black)">Book Bargain Mentor® Daniel R. Marston for Your Podcast</h3>

  <footer class="abs footer">
    <div class="footer-phone"><svg width="8" height="8" viewBox="0 0 24 24"><path fill="#fff" d="M6.6 10.8a15 15 0 0 0 6.6 6.6l2.2-2.2c.3-.3.7-.4 1-.2 1.1.4 2.3.6 3.6.6.6 0 1 .4 1 1V20c0 .6-.4 1-1 1A17 17 0 0 1 3 4c0-.6.4-1 1-1h3.5c.6 0 1 .4 1 1 0 1.3.2 2.5.6 3.6.1.3 0 .7-.2 1z"/></svg>555-014-2739</div>
    <div class="footer-links">
      <span><svg width="5" height="5"><circle cx="2.5" cy="2.5" r="2.2" fill="none" stroke="#fff" stroke-width=".8"/></svg>bargainmentor.net</span>
      <span><svg width="6" height="4"><rect x=".4" y=".4" width="5.2" height="3.2" fill="none" stroke="#fff" stroke-width=".8"/></svg>daniel@marstonmail.net</span>
      <span><svg width="5" height="5"><rect x=".4" y=".4" width="4.2" height="4.2" fill="none" stroke="#fff" stroke-width=".8"/></svg>network.example/in/danielmarston</span>
    </div>
  </footer>
</section>

</body>
</html>
```